Accountants Stationary Package

Letter head, compliment slip, business card, report cover

Using selected logo which will be supplied when available design with compliment slip, letter head, business card and report cover. Some information to be amended and will be supplied at revision stage, design needs to resonate with chosen logo.
Updates

Update information 1 business card - my name is "Martin Keeley" post numerals are FCA , TITLE = Managing Director, (but maybe chartered accountant) is ok, my personal mobile is 0417 55 58 66 and personal email ids martin.k@keeleyledger.com,au, I like the tag line included " everybody ....succcess" Don't want professional liability logo but ok with the PQ and tallo logo I like the colours I like the blue back where it has a soft watermark finish 2. letterheads Need logos for tallo, PQ, professional standards Needs full company name and ABN NUMmber as - Keeley Accounting Pty Limited, ACN 748 301 526 Linked in ? I am also ok with initials instead of icons for phone, email, fax mobile, etc

Industry/Entity Type

Accounting

Requirements
Must have
• Keeley Accounting Pty Limited
• ABN 456456456
• Charted accountants
• Telephone 612 48559302
• Fax 612 4857 1438
• Po Box 5864, Erina, NSW, 2250
• Mobile 0417 555 866
• Address 42 Wendover road, Brindle Bay, suite 3 Wendover Hub
• Mail@keeleyledger.com.au
• Website keeleyledger.com.au
• List of services;
• Tax and Accounting
• Business Development
• Superannuation and Financial Services

```html
<!DOCTYPE html>
<html lang="en">
<head>
<meta charset="utf-8">
<title>Keeley Accounting – Business Card</title>
<link href="https://fonts.googleapis.com/css2?family=Questrial&display=swap" rel="stylesheet">
<style>
  :root {
    --page: #e9e6e1;
    --card-light: #ffffff;
    --card-dark: #0b0d18;
    --blue: #29a8e0;
    --orange: #f26a2e;
    --green: #8cc63f;
    --wash-blue: #d4e4f5;
    --wash-peach: #fddccb;
    --wash-dark: #1b2631;
    --wash-rust: #2e1c1c;
  }
  * { box-sizing: border-box; margin: 0; padding: 0; }
  html, body { width: 1200px; height: 1200px; overflow: hidden; }
  body {
    background: var(--page);
    font-family: "Questrial", "Century Gothic", sans-serif;
    display: flex; flex-direction: column; align-items: center; justify-content: center;
    gap: 56px;
  }
  .card {
    position: relative; width: 880px; height: 515px; overflow: hidden;
    box-shadow: 0 8px 24px rgba(0,0,0,.18);
  }
  .card--front { background: var(--card-light); }
  .card--back { background: var(--card-dark); }
  .watermark { position: absolute; left: 0; top: 0; width: 330px; height: 515px; }
  .brand {
    position: absolute; display: flex; align-items: center; gap: 16px;
    white-space: nowrap;
  }
  .brand__square { width: 64px; height: 64px; background: var(--blue); flex: none; }
  .brand__name {
    font-size: 40px; color: var(--blue); letter-spacing: 1px; line-height: 1;
  }
  .card--front .brand { right: 72px; top: 50px; }
  .details {
    position: absolute; right: 72px; top: 160px; text-align: right;
    font-size: 22px; line-height: 27px; color: var(--blue); white-space: nowrap;
  }
  .details .gap { height: 16px; }
  .details .label { color: var(--orange); }
  .details .company { color: var(--green); }
  .contact { display: flex; justify-content: flex-end; align-items: center; gap: 8px; }
  .contact svg { width: 16px; height: 16px; flex: none; }
  .card--back .brand { left: 330px; right: 0; top: 190px; justify-content: center; }
  .card--back .brand__name { font-size: 36px; }
  .services {
    position: absolute; left: 330px; right: 0; top: 330px; text-align: center;
    font-size: 23px; line-height: 28px; color: var(--blue);
  }
</style>
</head>
<body>

<section class="card card--front" aria-label="Business card front">
  <svg class="watermark" viewBox="0 0 330 515" aria-hidden="true">
    <rect x="0" y="0" width="270" height="270" fill="var(--wash-blue)"/>
    <rect x="0" y="310" width="300" height="205" fill="var(--wash-peach)" opacity=".7"/>
  </svg>

  <div class="brand">
    <span class="brand__square"></span>
    <span class="brand__name">KEELEY ACCOUNTING</span>
  </div>

  <div class="details">
    <p><span class="label">ABN</span> 456456456</p>
    <p>Po Box 5864,</p>
    <p>Brindle Bay, NSW, 2291</p>
    <div class="gap"></div>
    <p class="contact">612 48559302
      <svg viewBox="0 0 16 16"><rect width="16" height="16" rx="2" fill="var(--orange)"/><path d="M5 3.5c-1 .6-1.2 2 0 4.2s2.6 3.8 4.5 4.5c1 .3 1.8 0 2.2-.8l-1.6-1.6-1.2.6C7.8 9.7 6.5 8.3 6 7.1l.6-1.2L5 3.5z" fill="#fff"/></svg></p>
    <p class="contact">612 4857 1438
      <svg viewBox="0 0 16 16"><rect x="4" y="1" width="8" height="4" fill="var(--orange)"/><rect x="1" y="6" width="14" height="6" rx="1" fill="var(--orange)"/><rect x="4" y="10" width="8" height="5" fill="var(--orange)"/><rect x="5" y="11.5" width="6" height="1" fill="#fff"/></svg></p>
    <p class="contact">Mail@keeleyledger.com.au
      <svg viewBox="0 0 16 16"><rect y="3" width="16" height="10" fill="var(--orange)"/><path d="M0 3l8 6 8-6" fill="none" stroke="#fff" stroke-width="1.2"/></svg></p>
    <p class="contact">keeleyledger.com.au
      <svg viewBox="0 0 16 16"><circle cx="8" cy="8" r="7" fill="none" stroke="var(--orange)" stroke-width="1.4"/><ellipse cx="8" cy="8" rx="3" ry="7" fill="none" stroke="var(--orange)" stroke-width="1.2"/><path d="M1 8h14M2 4.5h12M2 11.5h12" stroke="var(--orange)" stroke-width="1.1"/></svg></p>
    <div class="gap"></div>
    <p class="company">Keeley Accounting Pty Limited</p>
    <p>42 Wendover road, Brindle Bay,</p>
    <p>suite 3 Wendover Hub</p>
  </div>
</section>

<section class="card card--back" aria-label="Business card back">
  <svg class="watermark" viewBox="0 0 330 515" aria-hidden="true">
    <rect x="0" y="0" width="300" height="300" fill="var(--wash-dark)"/>
    <rect x="0" y="330" width="310" height="185" fill="var(--wash-rust)" opacity=".8"/>
  </svg>

  <div class="brand">
    <span class="brand__square"></span>
    <span class="brand__name">KEELEY ACCOUNTING</span>
  </div>

  <div class="services">
    <p>Tax and Accounting</p>
    <p>Business Development</p>
    <p>Superannuation and Financial Services</p>
  </div>
</section>

</body>
</html>
```